SEO AND WEB DESIGN COMPANY BUSINESS CARD DESIGN

I need an eye catching , simple business card design that will match my logo . I need 2 versions of it ( white background and black background) - SOME PEOPLE DID NOT GET IT AND SENDING US FRONT WHITE BACK WHITE VERSIONS WHICH IS NOT CORRECT.

ONE VERSION SHOULD BE BACK AND FRONT ALL BLACK , SECOND VERSION SHOULD BE BACK AND FRONT ALL WHITE

logo psd files are attached for both versions. The business card is going to have : First Name- Last name - position - phone numbers

```html
<!DOCTYPE html>
<html lang="en">
<head>
<meta charset="utf-8">
<title>Vela Studio – Business Card, Black Edition</title>
<link rel="stylesheet" href="https://fonts.googleapis.com/css2?family=Roboto:ital,wght@0,400;0,500;0,700;1,700&display=swap">
<style>
  :root {
    --stage: #3b3b3d;
    --card: #1f1f21;
    --card-edge: #2a2a2c;
    --mark: #2b2b2e;
    --ink: #f2f2f2;
    --ink-soft: #d9d9d9;
    --accent: #1ea0e6;
  }
  * { margin: 0; padding: 0; box-sizing: border-box; }
  html, body {
    width: 799px; height: 1200px; overflow: hidden;
    background: var(--stage);
    font-family: "Roboto", Arial, sans-serif;
  }
  .sheet {
    width: 799px; height: 1200px;
    display: flex; flex-direction: column;
    align-items: center; justify-content: space-around;
    padding: 60px 0;
  }
  .card {
    position: relative;
    width: 620px; height: 354px;
    background: var(--card);
    border: 1px solid var(--card-edge);
    box-shadow: 0 14px 30px rgba(0,0,0,.45);
  }
  /* front */
  .front-mark {
    position: absolute; left: 60px; top: 40px;
    width: 150px; height: 150px; border-radius: 50%;
    background: var(--mark);
  }
  .wordmark {
    position: absolute; right: 46px; bottom: 46px;
    font-weight: 700; font-size: 46px; letter-spacing: 1px;
    color: var(--ink); line-height: 1;
  }
  /* back */
  .person { position: absolute; left: 44px; top: 40px; }
  .person-name {
    font-weight: 700; font-style: italic; font-size: 20px;
    color: var(--accent);
  }
  .person-role { font-size: 14px; color: var(--ink); margin-top: 4px; }
  .contact {
    position: absolute; left: 44px; top: 168px;
    list-style: none; font-size: 15px; color: var(--ink-soft);
    line-height: 1.45;
  }
  .contact li { display: flex; align-items: center; gap: 10px; }
  .contact .plain { padding-left: 24px; }
  .contact svg { width: 14px; height: 14px; flex: none; }
  .back .wordmark { font-size: 40px; right: 40px; bottom: 40px; }
  .back .dot {
    position: absolute; right: 262px; bottom: 92px;
    width: 26px; height: 26px; border-radius: 50%;
    background: var(--accent);
  }
</style>
</head>
<body>
<main class="sheet">
  <section class="card front" aria-label="Card front">
    <div class="front-mark"></div>
    <div class="wordmark">Vela Studio</div>
  </section>

  <section class="card back" aria-label="Card back">
    <div class="person">
      <div class="person-name">Alex Marlow</div>
      <div class="person-role">Managing Director</div>
    </div>
    <ul class="contact">
      <li class="plain">58 Harbor Lane, Fairview,</li>
      <li class="plain">Northgate, US 204817</li>
      <li>
        <svg viewBox="0 0 16 16" aria-hidden="true"><path fill="#1ea0e6" d="M3.5 1.5l2.6 0 1 3.4-1.7 1.2a8 8 0 0 0 4.5 4.5l1.2-1.7 3.4 1v2.6c0 .8-.7 1.5-1.5 1.5A12.5 12.5 0 0 1 2 3c0-.8.7-1.5 1.5-1.5z"/></svg>
        555-014-2290
      </li>
      <li>
        <svg viewBox="0 0 16 16" aria-hidden="true"><rect x="1" y="3" width="14" height="10" fill="#1ea0e6"/><path d="M1 3l7 6 7-6" fill="none" stroke="#1f1f21" stroke-width="1.4"/></svg>
        alex@velastudio.com
      </li>
      <li>
        <svg viewBox="0 0 16 16" aria-hidden="true"><g fill="none" stroke="#1ea0e6" stroke-width="1.4"><circle cx="8" cy="8" r="6.5"/><ellipse cx="8" cy="8" rx="2.8" ry="6.5"/><path d="M1.5 8h13"/></g></svg>
        www.velastudio.com
      </li>
    </ul>
    <div class="dot"></div>
    <div class="wordmark">Vela Studio</div>
  </section>
</main>
</body>
</html>
```